New Wordpress, web design and a logo for a text analysis website. The website name is Quorvela.com

Task Description- We are looking for an exciting design for a new textual analysis website in Wordpress. The website enables individuals (initially only academics, but this might be expanded later) to upload textual data (e.g. excel files) for processing and download textual analysis results. For example, users can upload data with hundreds of Excel cells containing text and receive back analysis of the positive/negative sentiment in that text, the count of complex words, the count of numbers, the most frequent terms, or similarity of text in the uploaded database. The landing page will explain the concept and vision of the website, will perhaps visually illustrate the ease with which it can be done (files uploaded and results downloaded with no need for technical knowledge). Hence, we want to communicate that we provide an easy to use, yet powerful tool. Although we do not have images to share, we would like the website to include images and graphic images, you may use stock images in your design.

Logo- The design should include a logo with the word “Quorvela” and perhaps a magnifying glass enlarging text, but we are open to some creative thinking of the logo. Overall, we are hoping to communicate the following terms: “textual analysis” and “analytics”.
Pages- The design should include at least the following pages (each should include a logo, header, body, background, navigation menu and a footer)

1. Home page, describing the overall objective to enable easy analysis of textual data. The background/images should likely illustrate text going into a magnifying glass/a computer/ or another automation-related and graphs (pie chart, bar chart, etc.), or other outputs, are coming out of the other side. We are open to all other creative suggestions to illustrate this process.
2. Tools- this page will list the different textual analysis tools that the website is offering and briefly explain each. Each of these tools is a link to its own page where the tool can be applied. Examples of tools that will be included are (1) Count of words and numbers (2) sentiment analysis (3) custom uploaded dictionary of words analysis (4) Similarity analysis (5) N-gram analysis of frequent single or multiple words.
3. Design of one tool page (we will replicate the design ourselves for other tools)- Each page will include an explanation of the procedure and files the users should prepare. Each page should also include forms that allow the users to (1) Browse their computer to upload their text file (2) drop down select boxes (3) radio buttons or check boxes. We will change the number of these boxes ourselves in the future.
4. Registration/Login- a standard registration page, asking users for name (first and last), email, set a password and confirm it. And also, allowing existing users to login.
5. About page- a page that includes information about the two researchers, including a photo and a short text describing their background.
6. News- a page describing news and media mentions of the page and links to research papers that used the tool.
Colors- The project is developed by researchers from two universities and the colors of both schools should be incorporated into the design. The primary colors of red and blue should be prominent. The color codes are in the following links (1) https://brand.halvermoor.edu/guide/design-elements/colors/ (2) https://www.ostrander.edu/offices/marketing-communications/ostrander-brand/brand-assets/ostrander-color-palette

Quorvela

```html
<!DOCTYPE html>
<html lang="en">
<head>
<meta charset="utf-8">
<title>Quorvela — Text Analysis</title>
<link rel="stylesheet" href="https://fonts.googleapis.com/css2?family=Poppins:wght@400;500;600;700&display=swap">
<style>
:root{
  --navy:#1c2260;
  --navy-deep:#1b2062;
  --red:#e0524f;
  --blue:#5a71d9;
  --ink:#1e2358;
  --body:#5a5d72;
  --soft:#f4f5fb;
  --white:#fff;
}
*{box-sizing:border-box;margin:0;padding:0}
html,body{width:1200px;height:3920px;overflow:hidden}
body{font-family:'Poppins',sans-serif;color:var(--body);background:var(--white);position:relative}
.abs{position:absolute}
h1,h2,h3,h4{color:var(--ink);font-weight:700}
p{font-size:14px;line-height:22px}

/* header */
.brand{display:flex;align-items:center;gap:8px;font-weight:700;font-size:22px;color:var(--navy)}
.brand-dot{width:14px;height:14px;border-radius:50%;background:var(--red)}
.site-header{left:88px;top:18px;width:1024px;height:40px;display:flex;align-items:center}
.nav{margin-left:auto;display:flex;gap:25px;font-size:13px;font-weight:600;color:var(--ink);align-items:center}
.nav .active{color:var(--red)}
.nav .register{margin-left:22px}
.btn{display:inline-flex;align-items:center;justify-content:center;border-radius:16px;font-weight:600;font-size:13px;color:#fff;letter-spacing:.4px}
.btn-login{background:var(--blue);width:82px;height:26px;font-size:12px}

/* hero */
.hero-blob{left:440px;top:0;width:760px;height:680px;border-bottom-left-radius:380px;background:linear-gradient(160deg,#fff 20%,#eef0f8 100%)}
.hero-title{left:88px;top:288px;font-size:43px;line-height:45px;width:440px}
.hero-copy{left:88px;top:382px;width:380px;font-size:15px;line-height:22px}
.btn-upload{left:88px;top:436px;width:136px;height:30px;background:var(--red);font-size:13px}
.art{border-radius:18px}
.hero-art{left:600px;top:110px;width:460px;height:440px;background:linear-gradient(150deg,#dfe4fb,#8c97d8 60%,#e9735f)}

/* intro */
.intro-title{left:0;top:664px;width:1200px;text-align:center;font-size:33px;line-height:38px}
.intro-copy{left:0;top:752px;width:1200px;text-align:center;font-size:15px;line-height:23px}
.feature{width:340px;text-align:center}
.feature h3{font-size:18px;margin:14px 0 8px;font-weight:600}
.feature p{font-size:13px;line-height:22px}
.feature svg{display:block;margin:0 auto}

/* tools */
.tools-band{left:0;top:1010px;width:1200px;height:574px;background:linear-gradient(180deg,#fff 0%,var(--soft) 45%,#f1f2f9 100%)}
.tools-art{left:144px;top:1112px;width:396px;height:370px;background:linear-gradient(160deg,#eef0f6,#c9cde0 55%,#e45f52)}
.sect-title{font-size:33px;line-height:37px}
.sect-copy{font-size:13.5px;line-height:22px}
.checks{list-style:none;font-size:14px;line-height:24px}
.checks li{display:flex;align-items:center;gap:12px}
.checks svg{flex:none}

/* design */
.design-art{left:654px;top:1710px;width:426px;height:262px;background:linear-gradient(150deg,#eceef3,#4e5a9c 55%,#e0524f)}

/* templates band */
.templates-band{left:0;top:2061px;width:1200px;height:233px;background:var(--red)}
.templates-art{left:0;top:2040px;width:555px;height:330px;background:linear-gradient(140deg,#f58a80 0%,#8e98e4 45%,#f6c3c9 100%);border-radius:0 18px 18px 0}
.templates-title{left:646px;top:2138px;color:#fff;font-size:33px}
.templates-copy{left:646px;top:2184px;width:400px;color:#fff;font-size:14px;line-height:22px}

/* analysis grid */
.analysis-title{left:0;top:2436px;width:1200px;text-align:center;font-size:33px}
.analysis-sub{left:0;top:2482px;width:1200px;text-align:center;font-size:16px}
.item{width:290px}
.item h4{font-size:20px;font-weight:600;margin-bottom:6px}
.item p{font-size:13px;line-height:22px}

/* testimonials */
.testi-title{left:0;top:2928px;width:1200px;text-align:center;font-size:33px}
.footer-zone{left:0;top:3235px;width:1200px;height:685px;background:var(--navy-deep)}
.stack{background:#fff;border-radius:0 0 12px 12px}
.card{left:252px;top:2990px;width:696px;height:304px;background:#fff;border-radius:14px;box-shadow:0 12px 40px rgba(30,35,90,.08);text-align:center}
.card p{position:absolute;left:70px;top:112px;width:556px;font-size:15px;line-height:25px}
.card .name{position:absolute;left:0;top:202px;width:100%;color:var(--red);font-weight:600;font-size:16px}
.card .role{position:absolute;left:0;top:226px;width:100%;font-size:12px}
.dots{position:absolute;left:0;top:252px;width:100%;display:flex;justify-content:center;gap:5px}
.dots span{width:8px;height:8px;border-radius:50%;background:#d6d9ea}
.dots span:first-child{background:var(--red)}

/* cta */
.cta-title{left:88px;top:3410px;color:#fff;font-size:33px}
.cta-copy{left:88px;top:3458px;color:#fff;font-size:16px}
.btn-start{left:810px;top:3434px;width:148px;height:34px;background:var(--blue)}
.btn-more{left:964px;top:3434px;width:148px;height:34px;background:#2a307a}
.rule{left:88px;width:1024px;height:1px;background:rgba(255,255,255,.18)}

/* footer */
.footer-brand{left:88px;top:3640px;color:#fff;font-size:28px}
.footer-about{left:88px;top:3714px;width:310px;color:#fff;font-size:12.5px;line-height:20px}
.f-col h4{color:#fff;font-size:20px;font-weight:600;margin-bottom:10px}
.f-col ul{list-style:none;color:#fff;font-size:13.5px;line-height:27.5px}
.f-col p{color:#fff;font-size:13.5px}
.contact li{display:flex;align-items:center;gap:8px}
.email-field{margin-top:12px;width:208px;height:32px;border-radius:16px;background:#2f3578;color:#aeb3da;font-size:12.5px;padding:0 18px;display:flex;align-items:center}
.btn-sub{margin-top:8px;width:126px;height:32px;background:var(--red);font-size:12.5px}
.copyright{left:0;top:3886px;width:1200px;text-align:center;color:#fff;font-size:12.5px}
</style>
</head>
<body>

<div class="abs hero-blob"></div>

<header class="abs site-header">
  <div class="brand">Quorvela<span class="brand-dot"></span></div>
  <nav class="nav">
    <span class="active">Home</span><span>Tools</span><span>Design</span><span>About</span><span>News</span><span>Contact Us</span>
    <span class="register">Register</span>
    <span class="btn btn-login">LOGIN</span>
  </nav>
</header>

<h1 class="abs hero-title">Your path to academic success</h1>
<p class="abs hero-copy">Files uploaded and results downloaded with no need for technical knowledge</p>
<span class="abs btn btn-upload">UPLOAD FILE</span>
<div class="abs art hero-art" role="img" aria-label="Illustration of people feeding documents into a large typewriter under a magnifying glass"></div>

<h2 class="abs intro-title">Quorvela provides a fully featured<br>text analysis platform!</h2>
<p class="abs intro-copy">Text Analysis is a complex and specialized task. Quorvela makes it super<br>simple to extract insight from textual content.</p>

<div class="abs feature" style="left:88px;top:836px">
  <svg width="100" height="72" viewBox="0 0 100 72" fill="none" stroke="#3b4aa8" stroke-width="2.5"><circle cx="32" cy="32" r="22"/><circle cx="58" cy="32" r="22"/><path d="M20 32h8M62 32h8" /><path d="M62 38l20 28 4-12 12-2z" stroke="#e0524f"/></svg>
  <h3>Corpus Builder</h3>
  <p>Lorem Ipsum is simply dummy text of the<br>printing and typesetting industry.</p>
</div>
<div class="abs feature" style="left:430px;top:836px">
  <svg width="100" height="72" viewBox="0 0 100 72" fill="none" stroke-width="2.5"><rect x="26" y="2" width="38" height="66" rx="3" stroke="#3b4aa8"/><path d="M32 14l4 4 6-8M32 30l4 4 6-8M32 46l4 4 6-8" stroke="#e0524f"/><path d="M48 16h10M48 32h10M48 48h10M56 70h20" stroke="#3b4aa8"/></svg>
  <h3>Detailed Results</h3>
  <p>Lorem Ipsum is simply dummy text of the<br>printing and typesetting industry.</p>
</div>
<div class="abs feature" style="left:770px;top:836px">
  <svg width="100" height="72" viewBox="0 0 100 72" fill="none" stroke-width="2.5"><rect x="18" y="48" width="10" height="20" stroke="#3b4aa8"/><rect x="34" y="36" width="10" height="32" stroke="#e0524f"/><rect x="50" y="42" width="10" height="26" stroke="#3b4aa8"/><rect x="66" y="24" width="10" height="44" stroke="#e0524f"/><path d="M14 36l18-14 16 10 18-18 14-10" stroke="#3b4aa8"/><circle cx="32" cy="22" r="3" stroke="#e0524f"/><circle cx="66" cy="14" r="3" stroke="#e0524f"/></svg>
  <h3>Advanced Visualizations</h3>
  <p>Lorem Ipsum is simply dummy text of the<br>printing and typesetting industry.</p>
</div>

<div class="abs tools-band"></div>
<div class="abs art tools-art" role="img" aria-label="Illustration of a person with a laptop beside an upload files panel and floating documents"></div>
<h2 class="abs sect-title" style="left:620px;top:1214px">Tools Quorvela</h2>
<p class="abs sect-copy" style="left:622px;top:1257px;width:440px">Text Analysis is a complex and specialized task. Quorvela makes it super simple to extract insight from textual content.</p>
<ul class="abs checks" style="left:622px;top:1312px">
  <li><svg width="13" height="10" viewBox="0 0 13 10"><path d="M1 5l4 4 7-8" fill="none" stroke="#5cb85c" stroke-width="2"/></svg>Count of words and numbers</li>
  <li><svg width="13" height="10" viewBox="0 0 13 10"><path d="M1 5l4 4 7-8" fill="none" stroke="#5cb85c" stroke-width="2"/></svg>Sentiment analysis</li>
  <li><svg width="13" height="10" viewBox="0 0 13 10"><path d="M1 5l4 4 7-8" fill="none" stroke="#5cb85c" stroke-width="2"/></svg>Custom uploaded dictionary of words analysis</li>
  <li><svg width="13" height="10" viewBox="0 0 13 10"><path d="M1 5l4 4 7-8" fill="none" stroke="#5cb85c" stroke-width="2"/></svg>Similarity analysis</li>
  <li><svg width="13" height="10" viewBox="0 0 13 10"><path d="M1 5l4 4 7-8" fill="none" stroke="#5cb85c" stroke-width="2"/></svg>N-gram analysis of frequent single or multiple words.</li>
</ul>

<h2 class="abs sect-title" style="left:146px;top:1708px">Quorvela Design<br>of one tool</h2>
<p class="abs sect-copy" style="left:147px;top:1790px;width:430px">Text Analysis is a complex and specialized task. Quorvela makes it super simple to extract insight from textual content.</p>
<ul class="abs checks" style="left:147px;top:1846px;width:450px">
  <li><svg width="13" height="10" viewBox="0 0 13 10"><path d="M1 5l4 4 7-8" fill="none" stroke="#5cb85c" stroke-width="2"/></svg>Browse their computer to upload their text file</li>
  <li><svg width="13" height="10" viewBox="0 0 13 10"><path d="M1 5l4 4 7-8" fill="none" stroke="#5cb85c" stroke-width="2"/></svg>Drop down select boxes</li>
  <li style="align-items:flex-start"><svg width="13" height="10" viewBox="0 0 13 10" style="margin-top:7px"><path d="M1 5l4 4 7-8" fill="none" stroke="#5cb85c" stroke-width="2"/></svg>Radio buttons or check boxes. We will change the number of these boxes ourselves in the future.</li>
</ul>
<div class="abs art design-art" role="img" aria-label="Illustration of a person holding a folder surrounded by file type documents"></div>

<div class="abs templates-band"></div>
<div class="abs templates-art" role="img" aria-label="Illustration of documents, a search bar and a magnifying glass"></div>
<h2 class="abs templates-title">Quorvela Templates</h2>
<p class="abs templates-copy">Time-savings templates that you can download and edit in work or google docs.</p>

<h2 class="abs analysis-title">What analysis can Quorvela provide?</h2>
<p class="abs analysis-sub">Gain an understanding of your text with these language features below.</p>

<div class="abs item" style="left:122px;top:2554px"><h4>Nouns</h4><p>Lorem Ipsum is simply dummy text of the printing and typesetting industry .</p></div>
<div class="abs item" style="left:466px;top:2554px"><h4>Adjectives</h4><p>Lorem Ipsum is simply dummy text of the printing and typesetting industry .</p></div>
<div class="abs item" style="left:804px;top:2554px"><h4>Verbs</h4><p>Lorem Ipsum is simply dummy text of the printing and typesetting industry .</p></div>
<div class="abs item" style="left:122px;top:2664px"><h4>Prepositions</h4><p>Lorem Ipsum is simply dummy text of the printing and typesetting industry .</p></div>
<div class="abs item" style="left:466px;top:2664px"><h4>Topic Modeling</h4><p>Lorem Ipsum is simply dummy text of the printing and typesetting industry .</p></div>
<div class="abs item" style="left:804px;top:2664px"><h4>POS Tagger</h4><p>Lorem Ipsum is simply dummy text of the printing and typesetting industry .</p></div>
<div class="abs item" style="left:122px;top:2776px"><h4>Extract Dates</h4><p>Lorem Ipsum is simply dummy text of the printing and typesetting industry .</p></div>
<div class="abs item" style="left:466px;top:2776px"><h4>Word Clouds</h4><p>Lorem Ipsum is simply dummy text of the printing and typesetting industry .</p></div>
<div class="abs item" style="left:804px;top:2776px"><h4>Top Occurring Words</h4><p>Lorem Ipsum is simply dummy text of the printing and typesetting industry .</p></div>

<h2 class="abs testi-title">Testimonials</h2>

<div class="abs footer-zone"></div>
<div class="abs stack" style="left:345px;top:3300px;width:511px;height:36px;background:#f4f5fa"></div>
<div class="abs stack" style="left:289px;top:3280px;width:622px;height:36px;background:#fafbfe"></div>
<div class="abs card">
  <svg class="abs" style="left:300px;top:56px" width="96" height="70" viewBox="0 0 96 70"><path d="M4 70V40C4 18 16 4 40 0v12C28 16 22 24 22 34h18v36zM56 70V40C56 18 68 4 92 0v12C80 16 74 24 74 34h18v36z" fill="#eceef3"/></svg>
  <p>Lorem Ipsum is simply dummy text of the printing and typesetting industry. Lorem Ipsum has been the industry's standard dummy text ever since the 1500s, when ...</p>
  <div class="name">Miles Harrow</div>
  <div class="role">CO founder</div>
  <div class="dots"><span></span><span></span><span></span></div>
</div>

<h2 class="abs cta-title">Analyze your text today!</h2>
<p class="abs cta-copy">Time to finally do it in a way that's easy.</p>
<span class="abs btn btn-start">GET STARTED</span>
<span class="abs btn btn-more">LEARN MORE</span>
<div class="abs rule" style="top:3526px"></div>

<div class="abs brand footer-brand">Quorvela<span class="brand-dot"></span></div>
<p class="abs footer-about">Lorem Ipsum is simply dummy text of the printing and typesetting industry lorem Ipsum has been the industry's standard dummy .</p>

<div class="abs f-col" style="left:455px;top:3606px">
  <h4>Useful Links</h4>
  <ul><li>Home</li><li>Tools</li><li>Design</li><li>About</li><li>News</li><li>Contact Us</li></ul>
</div>
<div class="abs f-col" style="left:650px;top:3606px">
  <h4>Newsletter</h4>
  <p>Subscribe to our newletter</p>
  <div class="email-field">Email address</div>
  <span class="btn btn-sub">SUBSCRIBE</span>
</div>
<div class="abs f-col" style="left:926px;top:3606px">
  <h4>Contact us</h4>
  <ul class="contact">
    <li><svg width="11" height="13" viewBox="0 0 11 13"><path d="M5.5 13S0 7.5 0 5a5.5 5.5 0 0111 0c0 2.5-5.5 8-5.5 8z" fill="#e0524f"/><circle cx="5.5" cy="5" r="2" fill="#1b2062"/></svg>Some goes address here</li>
    <li><svg width="12" height="10" viewBox="0 0 12 10"><rect width="12" height="10" rx="1" fill="#e0524f"/><path d="M1 1l5 4 5-4" fill="none" stroke="#1b2062" stroke-width="1.2"/></svg>info@Quorvela.com</li>
    <li><svg width="12" height="12" viewBox="0 0 12 12"><path d="M2 0l3 3-1.5 2a7 7 0 003.5 3.5L9 7l3 3-2 2C5 12 0 7 0 2z" fill="#e0524f"/></svg>+145 ( 5528 ) 317</li>
    <li><svg width="12" height="12" viewBox="0 0 12 12"><circle cx="6" cy="6" r="6" fill="#e0524f"/><path d="M0 6h12M6 0c-3 3-3 9 0 12M6 0c3 3 3 9 0 12" fill="none" stroke="#1b2062" stroke-width=".9"/></svg>www.quorvela.com</li>
  </ul>
</div>

<div class="abs rule" style="top:3868px"></div>
<p class="abs copyright">Copyright 2021 | All Rights Reserved</p>

</body>
</html>
```